Flyer Design Project for Sports Medicine Services

I am a sports medicine doctor specialising in the diagnosis and management of sport and exercise injuries for all ages and levels of activity - from elite to weekend jogger. I work under the Business name Clear Stride Athletic Care and do have a company logo. I am wanting a flier that I can send to family doctors, physiotherapists and sports clubs explaining who I am what I can offer and why they should send me patients.
- I have a Masters in Sports Medicine (MSportsMed), Diplomas in Obstetrics/Gynaecology (DRANZCOG) and also Paediatrics (DCH) and certificate in advanced clinical hypnosis
-accurate diagnosis and management plan with their regular physio to return the player / athlete to the field / court /gym as soon as safely possible
-hypnosis for sports performance eg anxiety control, confidence and mental rehearsal for individuals and teams
- because there are many possible therapists and therapy options, as a sports doctor I can work out who they need to see a physiotherapist, surgeon, massage therapist chiropractor or podiatrist to return them to activity or whether cortisone, PRP or autologous blood injections are needed
-can provide one point of contact for coaches and clubs for rehabilitation and return to sport advice.
- work with Karen Holloway ex Australian Athlete, a Performance Strategist (NRB listed resource person) and registered Psychologist for best mental preparation for individuals teams and coach development
- can organise rapid access to MRI, ultrasound and specialist appointments if needed
-I work at 3 practices KineVista 518 Belford St Belford 86129437 Monday Wednesday Friday; Harrowgate Sports Clinic, 143 Harrowgate Rd, Adelaide 85917264 Tuesday Coastal Hawks Sports Medicine Clinic, Velloran Park 8561 3097 Thursday.
-facebook site clearstrideathleticcare
Updates
Hi All, just to clarify.. My name is Peter Dunstan and I am the sports doctor. My wife is Karen Holloway and she is the psychologist. The flier should mainly be advertising my sports medicine services and a byline ( or at least not the first line in the title) about the Performance Strategy and Coach development.
Target Market(s)
family doctors (GPs), Sporting Clubs, Physiotherapists
Industry/Entity Type
Massage
Look and feel

```html
<!DOCTYPE html>
<html lang="en">
<head>
<meta charset="utf-8">
<title>Clear Stride Athletic Care – Sports Medicine Services</title>
<link href="https://fonts.googleapis.com/css2?family=Raleway:wght@500;600;700;800&display=swap" rel="stylesheet">
<style>
  :root {
    --sky: #b4e6f6;
    --sky-veil: rgba(178, 229, 246, 0.72);
    --teal: #8fd2d9;
    --ink: #3c474c;
    --white: #ffffff;
    --green: #2aa34c;
    --navy: #174d86;
    --logo-blue: #1f8fd1;
    --bar: #0d0d0d;
    --rule: #9a9a9a;
  }
  * { box-sizing: border-box; margin: 0; padding: 0; }
  html, body { width: 865px; height: 1200px; overflow: hidden; background: var(--white); }
  body { font-family: "Raleway", Arial, sans-serif; color: var(--ink); }
  .flyer { position: relative; width: 865px; height: 1200px; overflow: hidden; background: var(--white); }

  .treatment-photo {
    position: absolute; left: 0; top: 185px; width: 865px; height: 825px;
    background: linear-gradient(160deg, #f3ece6 0%, #e8cdb8 35%, #d9b39a 55%, #f1e2d6 78%, #f7f2ee 100%);
  }
  .hero-panel {
    position: absolute; left: 15px; top: 0; width: 835px; height: 823px;
    background: linear-gradient(to bottom, var(--sky) 0, var(--sky) 185px, var(--sky-veil) 260px, var(--sky-veil) 100%);
  }

  .brand {
    position: absolute; left: 15px; top: 34px; width: 120px; height: 105px;
    background: var(--white); display: flex; flex-direction: column; align-items: center; justify-content: center; gap: 6px;
  }
  .brand-dot { width: 30px; height: 30px; border-radius: 50%; background: var(--logo-blue); }
  .brand-name { font-size: 11px; font-weight: 700; color: var(--logo-blue); text-align: center; line-height: 1.15; }

  .contact-badge { position: absolute; left: 590px; top: -60px; width: 320px; height: 320px; }
  .badge-text {
    position: absolute; left: 640px; top: 0; width: 230px; text-align: center; color: var(--ink); font-weight: 700;
  }
  .badge-lead { font-size: 16px; line-height: 18px; }
  .badge-big { font-size: 34px; line-height: 38px; font-weight: 800; }
  .badge-small { font-size: 16px; line-height: 19.5px; margin-top: 2px; }

  .headline { position: absolute; left: 58px; top: 200px; color: var(--white); font-weight: 700; }
  .headline-lead { font-size: 34px; letter-spacing: 0.5px; }
  .headline-main { margin-left: 45px; margin-top: 6px; font-size: 88px; line-height: 78px; letter-spacing: 1px; }

  .services { position: absolute; left: 48px; top: 467px; width: 705px; list-style: none; }
  .service { position: relative; height: 73px; margin-bottom: 38px; }
  .service-box {
    position: absolute; left: 22px; top: 22px; right: 0; height: 72px;
    background: var(--white); border-radius: 18px; padding: 12px 20px 0 28px;
    font-size: 15px; font-weight: 700; line-height: 19.5px; color: var(--ink);
  }
  .service-check { position: absolute; left: 0; top: 0; width: 46px; height: 46px; }

  .doctor-photo {
    position: absolute; left: 16px; top: 1018px; width: 187px; height: 165px;
    background: linear-gradient(180deg, #5c8a3c 0%, #7fa552 40%, #c9b8a8 70%, #efe6e2 100%);
  }
  .team-card {
    position: absolute; left: 207px; top: 1018px; width: 643px; height: 97px;
    border: 1px solid var(--rule); background: var(--white);
  }
  .person { position: absolute; top: 2px; }
  .person-lead { left: 4px; }
  .person-partner { left: 375px; }
  .name-pill {
    display: inline-block; background: var(--navy); color: var(--white);
    font-size: 16px; font-weight: 700; padding: 4px 30px; border-radius: 14px; letter-spacing: 0.3px;
  }
  .credentials { list-style: none; margin-top: 5px; margin-left: 6px; font-size: 10.5px; font-weight: 700; line-height: 14.5px; color: #222; }
  .person-partner .credentials { width: 255px; }
  .amp { position: absolute; left: 300px; top: 24px; font-size: 44px; font-weight: 800; color: var(--navy); }

  .locations {
    position: absolute; left: 207px; top: 1119px; width: 643px; height: 64px;
    background: var(--bar); color: var(--white); padding: 4px 0 0 16px; list-style: none;
  }
  .location { display: flex; align-items: center; height: 18.5px; font-size: 11px; font-weight: 700; letter-spacing: 0.2px; }
  .location-address { margin-right: 8px; }
  .day-pill {
    display: inline-block; background: var(--white); color: #111; font-size: 7.5px; font-weight: 700;
    border-radius: 6px; padding: 1px 0; width: 62px; text-align: center; margin-right: 2px;
  }
</style>
</head>
<body>
<main class="flyer">
  <div class="treatment-photo" role="img" aria-label="Photo of a practitioner's hands treating an athlete's lower leg on a treatment table"></div>
  <div class="hero-panel"></div>

  <div class="brand">
    <span class="brand-dot"></span>
    <span class="brand-name">Clear Stride<br>Athletic Care</span>
  </div>

  <svg class="contact-badge" viewBox="0 0 320 320" aria-hidden="true">
    <circle cx="160" cy="160" r="140" fill="var(--teal)"/>
    <circle cx="160" cy="160" r="142" fill="none" stroke="var(--teal)" stroke-width="14" stroke-linecap="round" stroke-dasharray="0 19.5"/>
  </svg>
  <div class="badge-text">
    <p class="badge-lead">CAN PROVIDE</p>
    <p class="badge-big">1 POINT<br>OF<br>CONTACT</p>
    <p class="badge-small">FOR COACHES AND CLUBS<br>FOR REHABILIT-<br>ATION AND RETURN<br>TO SPORT<br>ADVICE.</p>
  </div>

  <h1 class="headline">
    <span class="headline-lead">ARE YOU LOOKING FOR</span>
    <span class="headline-main" style="display:block">SPORTS<br>MEDICINE<br>SERVICES?</span>
  </h1>

  <ul class="services">
    <li class="service">
      <div class="service-box">ACCURATE DIAGNOSIS AND MANAGEMENT PLAN WITH THEIR REGULAR PHYSIO TO RETURN THE PLAYER / ATHLETE TO THE FIELD / COURT /GYM AS SOON AS SAFELY POSSIBLE</div>
      <svg class="service-check" viewBox="0 0 46 46" aria-hidden="true"><circle cx="23" cy="23" r="23" fill="var(--green)"/><path d="M13 23.5l7 7 13-13" fill="none" stroke="#fff" stroke-width="4" stroke-linecap="round" stroke-linejoin="round"/></svg>
    </li>
    <li class="service">
      <div class="service-box">HYPNOSIS FOR SPORTS PERFORMANCE EG ANXIETY CONTROL, CONFIDENCE AND MENTAL REHEARSAL FOR INDIVIDUALS AND TEAMS</div>
      <svg class="service-check" viewBox="0 0 46 46" aria-hidden="true"><circle cx="23" cy="23" r="23" fill="var(--green)"/><path d="M13 23.5l7 7 13-13" fill="none" stroke="#fff" stroke-width="4" stroke-linecap="round" stroke-linejoin="round"/></svg>
    </li>
    <li class="service">
      <div class="service-box">- CAN ORGANISE RAPID ACCESS TO MRI, ULTRASOUND AND SPECIALIST APPOINT-MENTS IF NEEDED</div>
      <svg class="service-check" viewBox="0 0 46 46" aria-hidden="true"><circle cx="23" cy="23" r="23" fill="var(--green)"/><path d="M13 23.5l7 7 13-13" fill="none" stroke="#fff" stroke-width="4" stroke-linecap="round" stroke-linejoin="round"/></svg>
    </li>
  </ul>

  <div class="doctor-photo" role="img" aria-label="Portrait photo of Dr Peter Dunstan seated outdoors in front of garden foliage"></div>

  <section class="team-card">
    <div class="person person-lead">
      <span class="name-pill">PETER DUNSTAN</span>
      <ul class="credentials">
        <li>MASTERS IN SPORTS MEDICINE</li>
        <li>DIPLOMAS IN OBSTETRICS/GYNAECOLOGY</li>
        <li>PAEDIATRICS (DCH)</li>
        <li>CERTIFICATE IN ADVANCED CLINICAL HYPNOSIS</li>
      </ul>
    </div>
    <span class="amp">&amp;</span>
    <div class="person person-partner">
      <span class="name-pill">KAREN HOLLOWAY</span>
      <ul class="credentials">
        <li>EX AUSTRALIAN ATHLETE</li>
        <li>PERFORMANCE STRATEGIST (NRB LISTED RESOURCE PERSON)</li>
        <li>REGISTERED PSYCHOLOGIST</li>
      </ul>
    </div>
  </section>

  <ul class="locations">
    <li class="location"><span class="location-address">KINEVISTA 518 BELFORD ST BELFORD 86129437</span><span class="day-pill">MONDAY</span><span class="day-pill">WEDNESDAY</span><span class="day-pill">FRIDAY</span></li>
    <li class="location"><span class="location-address">HARROWGATE SPORTS CLINIC, 143 HARROWGATE RD, ADELAIDE 85917264</span><span class="day-pill">TUESDAY</span></li>
    <li class="location"><span class="location-address">COASTAL HAWKS SPORTS MEDICINE CLINIC, VELLORAN PARK 8561 3097</span><span class="day-pill">THURSDAY</span></li>
  </ul>
</main>
</body>
</html>
```